Velvet Dune is a premium Spa and Salon only professional tanning brand.

We need a email template/newsletter that we can send to our client base any time we would like to share information with them.
Whether this is launching our Christmas gift, or sharing up and coming training dates it will be another avenue for us to stay in touch with our clients.
We like to think ourselves as the 'Marchetti handbag' in the tanning world, Velvet Dune is a brand that is desirable and exclusive and has people hooked once they trial the brand and are blown away by the results.
www.velvet-dune.com

```html
<!DOCTYPE html>
<html lang="en">
<head>
<meta charset="utf-8">
<title>Velvet Dune Newsletter</title>
<link href="https://fonts.googleapis.com/css2?family=Anton&family=Arimo:wght@400;700&display=swap" rel="stylesheet">
<style>
:root{
  --brown:#7a3833;
  --brown-dark:#6a2a24;
  --brown-text:#7a2e26;
  --beige:#ebe5e1;
  --beige-line:#d9cfc8;
  --gold:#f6b51c;
  --gold-dark:#e89a10;
  --ink:#3a3330;
  --muted:#8a9aa6;
  --link:#2a6fa8;
  --white:#ffffff;
}
*{box-sizing:border-box;margin:0;padding:0}
html,body{width:1200px;height:3905px;overflow:hidden;background:var(--white)}
body{position:relative;font-family:"Arimo",Arial,sans-serif;color:var(--ink)}
.abs{position:absolute}
p{font-size:21px;line-height:29px}
.top-bar{left:44px;top:0;width:1108px;height:20px;background:linear-gradient(90deg,var(--brown-dark),#a07760,var(--brown-dark))}
.dateline{left:70px;top:60px;font-size:19px;font-weight:700;color:var(--muted);display:flex;align-items:center;gap:10px}
.viewline{right:68px;top:60px;font-size:18px;color:var(--muted)}
.viewline b{color:var(--link);text-decoration:underline}
.hero-frame{left:44px;top:125px;width:1108px;height:912px;background:var(--brown)}
.hero-photo{left:54px;top:143px;width:1088px;height:546px;background:radial-gradient(circle at 75% 35%,#e9c4a5,#b8703f 45%,#5a2c17)}
.hero-logo{left:100px;top:190px;font-size:52px;font-weight:700;color:var(--white);letter-spacing:2px}
.intro{left:54px;top:689px;width:1088px;height:346px;background:var(--beige)}
.intro h1{position:absolute;left:40px;top:56px;font-family:"Anton",Impact,sans-serif;font-weight:400;font-size:58px;color:var(--brown-text)}
.intro p{position:absolute;left:40px;top:136px;width:800px}
.intro .seal{position:absolute;left:868px;top:104px}
.lead-title{left:62px;top:1071px;width:705px;height:182px;background:var(--brown);color:var(--white);font-family:"Anton",Impact,sans-serif;font-size:58px;line-height:76px;padding:14px 20px}
.lead-sub{left:62px;top:1284px;width:705px;height:76px;background:var(--brown);color:var(--white);padding:10px 16px}
.lead-sub p{font-size:20px;line-height:27px}
.lead-photo{left:62px;top:1396px;width:705px;height:367px;background:linear-gradient(90deg,#3b1c12,#8a4a2a 45%,#d8a88a 70%,#6a3020)}
.lead-body{left:62px;top:1790px;width:705px}
.read-more{display:flex;align-items:center;gap:8px;font-size:20px;font-weight:700;color:var(--ink)}
.side-card{left:800px;top:1071px;width:336px;height:614px;background:var(--beige)}
.side-card h3{height:68px;background:var(--brown);color:var(--white);font-size:26px;font-weight:400;padding:20px 18px}
.side-product{position:absolute;left:16px;top:120px;width:304px;height:214px;background:var(--white)}
.side-product div{position:absolute;left:90px;top:30px;width:130px;height:160px;background:linear-gradient(90deg,#e6e2de,#fff,#d8d2cc)}
.side-card p{position:absolute;left:18px;top:362px;width:300px;font-size:20px;line-height:28px}
.side-card .read-more{position:absolute;left:18px;top:565px}
.offer-card{left:800px;top:1742px;width:336px;height:377px;border:2px solid var(--brown);background:var(--white)}
.offer-top{height:255px;background:var(--brown);color:var(--white);position:relative}
.offer-top .icon{position:absolute;left:20px;top:30px;width:100px;height:70px;background:linear-gradient(#f2d8c4,#c08a6a)}
.offer-top h3{position:absolute;left:136px;top:38px;font-size:26px;line-height:31px}
.offer-top p{position:absolute;left:20px;top:150px;width:290px;font-size:19px;line-height:27px}
.btn{display:flex;align-items:center;justify-content:center;gap:12px;background:linear-gradient(var(--gold),var(--gold-dark));border-radius:6px;font-weight:700;color:var(--brown-dark)}
.offer-card .btn{position:absolute;left:82px;top:288px;width:210px;height:52px;font-size:25px}
.dots{left:44px;width:1108px;height:0;border-top:5px dotted var(--beige-line)}
.section-head{left:0;top:2180px;width:1200px;text-align:center}
.section-head h2{font-family:"Anton",Impact,sans-serif;font-weight:400;font-size:56px;color:var(--brown-text)}
.section-head p{font-size:19px;color:var(--brown-text);margin-top:6px}
.tile{width:520px;height:510px;background:var(--beige)}
.tile .ph{height:216px}
.tile h3{position:absolute;left:34px;top:248px;font-size:28px;color:var(--brown-text);font-weight:700}
.tile p{position:absolute;left:34px;top:298px;width:460px;font-size:20px;line-height:28px}
.tile .read-more{position:absolute;left:34px;top:440px}
.connect{left:62px;top:2873px;width:1074px;height:286px;background:var(--beige)}
.connect h3{font-size:28px;font-weight:400;color:var(--brown-text);position:absolute}
.connect p{position:absolute;font-size:20px;line-height:28px}
.gift-list{position:absolute;left:762px;top:94px;list-style:none}
.gift-list li{font-size:20px;color:var(--brown-text);margin-bottom:24px;display:flex;align-items:center;gap:14px}
.gift-list li::before{content:"";border-left:9px solid var(--brown-text);border-top:7px solid transparent;border-bottom:7px solid transparent}
.cta{left:62px;top:3203px;width:1074px;height:159px;border:3px solid var(--brown)}
.cta h3{position:absolute;left:36px;top:36px;font-size:38px;font-weight:400;color:var(--brown-text)}
.cta p{position:absolute;left:36px;top:92px;font-size:20px;color:var(--brown-text)}
.cta .btn{position:absolute;left:648px;top:32px;width:362px;height:90px;font-family:"Anton",Impact,sans-serif;font-weight:400;font-size:40px}
.find-us{left:0;top:3460px;width:1200px;text-align:center;font-size:20px;color:var(--muted)}
.socials{left:0;top:3526px;width:1200px;display:flex;justify-content:center;gap:22px}
.socials span{width:62px;height:62px;border-radius:50%;background:radial-gradient(circle at 40% 35%,#ffffff,#dcdcdc);border:2px solid #cfcfcf}
.copyright{left:62px;top:3630px;font-size:16px}
.copyright u,.unsub u{color:var(--ink)}
.unsub{right:64px;top:3630px;font-size:16px}
.footer-logo{left:62px;top:3758px;font-size:46px;font-weight:700;color:var(--brown-text);line-height:50px}
.footer-address{left:430px;top:3745px;font-size:20px;line-height:28px;font-weight:700;color:var(--brown-text)}
.footer-contact{left:770px;top:3760px;font-size:28px;font-weight:700;color:var(--brown-text);line-height:38px}
.footer-contact div{display:flex;align-items:center;gap:14px}
</style>
</head>
<body>
<div class="abs top-bar"></div>
<div class="abs dateline">
  <svg width="20" height="20" viewBox="0 0 20 20"><rect x="2" y="4" width="16" height="14" fill="#f6a21c"/><rect x="2" y="4" width="16" height="4" fill="#d6801a"/></svg>
  Monday, September 8, 2014
</div>
<div class="abs viewline">If you are having trouble viewing images, please <b>click here.</b></div>

<div class="abs hero-frame"></div>
<div class="abs hero-photo" role="img" aria-label="Woman relaxing during a spa back massage"></div>
<div class="abs hero-logo">Velvet Dune</div>

<section class="abs intro">
  <h1>Lorem Ipsum</h1>
  <p>Vestibulum dapibus, mauris nec malesuada fames ac turpis velit, rhoncus eu, luctus et interdum adipiscing wisi. Aliquam erat ac ipsum. Integer aliquam purus. Phasellus fermentum in, dolor. Pellentesque facilisis. Nulla imperdiet sit amet magna. Vestibulum dapibus, mauris nec malesuada fames ac turpis velit, rhoncus eu, luctus et interdum adipiscing wisi. Aliquam erat ac ipsum.</p>
  <svg class="seal" width="190" height="190" viewBox="0 0 190 190" role="img" aria-label="Certification seal"><circle cx="95" cy="95" r="88" fill="none" stroke="#9c5a3c" stroke-width="6"/><circle cx="95" cy="95" r="62" fill="#9c5a3c"/></svg>
</section>

<div class="abs lead-title">Nullam viverra dolor consectetuer</div>
<div class="abs lead-sub"><p>Vestibulum dapibus, mauris nec malesuada fames ac turpis velit, rhoncus eu, luctus et interdum adipiscing wisi. Aliquam erat ac ipsum.</p></div>
<div class="abs lead-photo" role="img" aria-label="Chocolate face mask treatment beside a bowl of mask cream"></div>
<div class="abs lead-body">
  <p>Vestibulum dapibus, mauris nec malesuada fames ac turpis velit, rhoncus eu, luctus et interdum adipiscing wisi. Aliquam erat ac ipsum. Integer aliquam purus. Quisque lorem tortor fringilla sed, vestibulum id, eleifend justo vel bibendum sapien massa ac turpis faucibus. Quisque cursus et, porttitor risus. Aliquam sem. In hendrerit nulla quam nunc, accumsan congue. Lorem ipsum primis in nibh vel risus. Sed vel lectus. Ut sagittis, ipsum dolor quam.</p>
  <div class="read-more" style="justify-content:flex-end;margin-top:38px">
    <svg width="20" height="20" viewBox="0 0 20 20"><circle cx="10" cy="10" r="10" fill="#3a3330"/><path d="M8 5l5 5-5 5z" fill="#fff"/></svg>Read More
  </div>
</div>

<aside class="abs side-card">
  <h3>Nullam viverra</h3>
  <div class="side-product" role="img" aria-label="Tanning product bottles"><div></div></div>
  <p>Quisque lorem tortor fringilla sed, vestibulum id, eleifend justo vel bibendum sapien massa faucibus orci luctus non quis.</p>
  <div class="read-more"><svg width="20" height="20" viewBox="0 0 20 20"><circle cx="10" cy="10" r="10" fill="#3a3330"/><path d="M8 5l5 5-5 5z" fill="#fff"/></svg>Read More</div>
</aside>

<aside class="abs offer-card">
  <div class="offer-top">
    <div class="icon" role="img" aria-label="Mortar and pestle illustration"></div>
    <h3>Suspendisse pellentesque</h3>
    <p>Quisque lorem tortor fringilla sed, vestibulum id, eleifend.</p>
  </div>
  <div class="btn">
    <svg width="26" height="22" viewBox="0 0 26 22"><path d="M1 3h5l3 12h13l3-9H8" fill="none" stroke="#6a2a24" stroke-width="3"/><circle cx="11" cy="19" r="2.5" fill="#6a2a24"/><circle cx="20" cy="19" r="2.5" fill="#6a2a24"/></svg>
    Buy Item
  </div>
</aside>

<div class="abs dots" style="top:2153px"></div>

<header class="abs section-head">
  <h2>Quisque lorem tortor fringilla sed, vestibulum</h2>
  <p>Pellentesque facilisis. Nulla imperdiet sit amet magna.</p>
</header>

<article class="abs tile" style="left:62px;top:2332px">
  <div class="ph" role="img" aria-label="Candlelit spa massage room" style="background:linear-gradient(120deg,#3a1a14,#8a3a30 50%,#d8c0a8)"></div>
  <h3>Nullam viverra consectetuer</h3>
  <p>Ut molestie a, ultricies porta urna. Vestibulum commodo volutpat a, convallis ac, laoreet enim. Pellentesque facilisis. Nulla imperdiet sit amet magna.</p>
  <div class="read-more"><svg width="20" height="20" viewBox="0 0 20 20"><circle cx="10" cy="10" r="10" fill="#3a3330"/><path d="M8 5l5 5-5 5z" fill="#fff"/></svg>Read More</div>
</article>
<article class="abs tile" style="left:616px;top:2332px">
  <div class="ph" role="img" aria-label="Relaxing facial massage treatment" style="background:linear-gradient(120deg,#d89a70,#f3dcc8 55%,#fbf1e8)"></div>
  <h3>Nullam viverra consectetuer</h3>
  <p>Ut molestie a, ultricies porta urna. Vestibulum commodo volutpat a, convallis ac, laoreet enim. Pellentesque facilisis. Nulla imperdiet sit amet magna.</p>
  <div class="read-more"><svg width="20" height="20" viewBox="0 0 20 20"><circle cx="10" cy="10" r="10" fill="#3a3330"/><path d="M8 5l5 5-5 5z" fill="#fff"/></svg>Read More</div>
</article>

<section class="abs connect">
  <svg style="position:absolute;left:36px;top:80px" width="140" height="120" viewBox="0 0 140 120"><rect x="4" y="30" width="132" height="86" fill="#8a3e32"/><path d="M4 30l66 52 66-52" fill="none" stroke="#ebe5e1" stroke-width="5"/><rect x="30" y="4" width="80" height="60" fill="#fff" opacity=".85"/></svg>
  <h3 style="left:206px;top:36px">Keep in touch</h3>
  <p style="left:206px;top:86px;width:300px">Quisque lorem tortor fringilla sed, vestibulum id, eleifend justo vel bibendum sapien massa faucibus orci luctus non quis.</p>
  <svg style="position:absolute;left:596px;top:66px" width="132" height="140" viewBox="0 0 132 140"><rect x="6" y="40" width="120" height="28" fill="#8a3e32"/><rect x="16" y="72" width="100" height="64" fill="#8a3e32"/><rect x="58" y="40" width="16" height="96" fill="#ebe5e1"/><path d="M66 38C50 6 30 10 36 30zM66 38C82 6 102 10 96 30z" fill="#8a3e32"/></svg>
  <h3 style="left:762px;top:36px">Gift Zone</h3>
  <ul class="gift-list">
    <li>Quisque lorem fringilla</li>
    <li>Quisque lorem</li>
    <li>Nulla ipsum dolor</li>
  </ul>
</section>

<section class="abs cta">
  <h3>Nullam viverra consectetuer</h3>
  <p>Quisque lorem tortor fringilla vestibulum eleifend.</p>
  <div class="btn">See What’s Hot!</div>
</section>

<div class="abs dots" style="top:3398px"></div>

<div class="abs find-us">Find us:</div>
<div class="abs socials" aria-label="Social links">
  <span></span><span></span><span></span><span></span><span></span><span></span>
</div>

<div class="abs copyright">Copyright © 2014 <u>Velvet Dune</u> Ltd.</div>
<div class="abs unsub">You are currently signed up to Company's newsletters. <u>To unsubscribe click here</u></div>

<div class="abs dots" style="top:3687px"></div>

<footer>
  <div class="abs footer-logo">Velvet<br>Dune</div>
  <address class="abs footer-address" style="font-style:normal">Harrowgate Business Park<br>Linden Mill Road<br>Ashcombe, County Wexmoor AC14 7LZ</address>
  <div class="abs footer-contact">
    <div><svg width="22" height="32" viewBox="0 0 22 32"><rect x="2" y="1" width="18" height="30" rx="3" fill="none" stroke="#7a2e26" stroke-width="3"/><circle cx="11" cy="26" r="2" fill="#7a2e26"/></svg>1-800-0000-000</div>
    <div><svg width="26" height="20" viewBox="0 0 26 20"><rect x="1" y="1" width="24" height="18" fill="none" stroke="#7a2e26" stroke-width="3"/><path d="M1 1l12 10 12-10" fill="none" stroke="#7a2e26" stroke-width="3"/></svg>hello@velvet-dune.com</div>
  </div>
</footer>
</body>
</html>
```